Decorative concrete business needs new business cards

Our company attracts homeowners and business with disposable cash. We are a artistic decorative coatings company that will transform your driveway, patio, floors or counter tops into a work of art. We also engrave logos and designs right into the concrete! We are upscale and very professional company. I am open for rearranging our logo on the business card and also to different color patterns. We like the blue and black as in Brandquill's logo. We also like blue and orange/yellow.

Target Market(s)

Adults 30-70

Industry/Entity Type

Concrete

Contact Information for Business Card

Simple: Name, phone, email, website and social media icons

Font styles to use
Serif

Colors

Designer to choose colors to be used in the design.

Requirements
Must have
• Must present a professional upscale appearance. I have attached before and after photos that show you what our industry does. Maybe I will have before and after photo on back of card.
Nice to have
• Artistic, but bold. Nothing whimsical or cute.
Should not have
• Should not have cartoon or childlike appearance.

```html
<!DOCTYPE html>
<html lang="en">
<head>
<meta charset="utf-8">
<title>Stonecrest Coatings – Business Cards</title>
<link rel="stylesheet" href="https://fonts.googleapis.com/css2?family=Montserrat:wght@400;500;600&display=swap">
<style>
  :root {
    --stage: #e4e4e4;
    --card: #ffffff;
    --ink: #1a1a1a;
    --blue: #2f8fc6;
    --orange: #ef9a1e;
    --grey: #6f6f6f;
    --rule: #9a9a9a;
  }
  * { margin: 0; padding: 0; box-sizing: border-box; }
  html, body { width: 1200px; height: 864px; overflow: hidden; }
  body {
    background: var(--stage);
    font-family: "Montserrat", sans-serif;
    display: flex;
    flex-direction: column;
    align-items: center;
    justify-content: center;
    gap: 36px;
  }
  .card {
    width: 660px;
    height: 378px;
    background: var(--card);
    box-shadow: 0 6px 18px rgba(0,0,0,.18);
    position: relative;
  }
  .wordmark {
    display: flex;
    align-items: center;
    gap: 14px;
    font-weight: 600;
    color: var(--ink);
    letter-spacing: .04em;
    text-transform: uppercase;
    line-height: 1;
  }
  .wordmark-square {
    width: 34px; height: 34px;
    background: var(--blue);
    flex: none;
  }
  .wordmark-name { font-size: 34px; }

  /* Front */
  .card-front {
    display: flex;
    flex-direction: column;
    align-items: center;
    justify-content: center;
  }
  .card-front .wordmark { margin-top: 10px; }
  .front-url {
    position: absolute;
    bottom: 78px;
    left: 0; right: 0;
    text-align: center;
    font-size: 15px;
    color: var(--grey);
    letter-spacing: .02em;
  }

  /* Back */
  .card-back {
    display: flex;
    align-items: center;
    padding: 0 40px 0 44px;
  }
  .card-back .wordmark { gap: 12px; }
  .card-back .wordmark-name { font-size: 26px; }
  .divider {
    width: 1px;
    height: 170px;
    background: var(--rule);
    margin: 0 30px 0 26px;
    flex: none;
  }
  .contact-block { display: flex; flex-direction: column; }
  .person-name { font-size: 22px; font-weight: 600; color: var(--blue); }
  .person-title { font-size: 15px; color: var(--grey); margin: 2px 0 20px 10px; }
  .contact-list { list-style: none; display: flex; flex-direction: column; gap: 6px; }
  .contact-item {
    display: flex; align-items: center; gap: 10px;
    font-size: 15px; color: var(--grey);
  }
  .contact-item svg { width: 14px; height: 14px; flex: none; }
</style>
</head>
<body>

<section class="card card-front" aria-label="Card front">
  <div class="wordmark">
    <span class="wordmark-square"></span>
    <span class="wordmark-name">Stonecrest Coatings</span>
  </div>
  <p class="front-url">www.yourwebsite.com</p>
</section>

<section class="card card-back" aria-label="Card back">
  <div class="wordmark">
    <span class="wordmark-square"></span>
    <span class="wordmark-name">Stonecrest<br>Coatings</span>
  </div>
  <div class="divider"></div>
  <div class="contact-block">
    <h1 class="person-name">Daniel Reyes</h1>
    <p class="person-title">President</p>
    <ul class="contact-list">
      <li class="contact-item">
        <svg viewBox="0 0 16 16" aria-hidden="true"><path fill="var(--orange)" d="M4 1l3 3-2 2c1 2 3 4 5 5l2-2 3 3-2 3C7 15 1 9 1 3z"/></svg>
        012-345-6789
      </li>
      <li class="contact-item">
        <svg viewBox="0 0 16 16" aria-hidden="true"><rect x="4" y="1" width="8" height="14" rx="1.5" fill="none" stroke="var(--orange)" stroke-width="1.6"/><circle cx="8" cy="12.5" r="1" fill="var(--orange)"/></svg>
        012-345-6780
      </li>
      <li class="contact-item">
        <svg viewBox="0 0 16 16" aria-hidden="true"><rect x="1" y="3" width="14" height="10" fill="var(--orange)"/><path d="M1 3l7 6 7-6" fill="none" stroke="#fff" stroke-width="1.3"/></svg>
        info@yourwebsite.com
      </li>
      <li class="contact-item">
        <svg viewBox="0 0 16 16" aria-hidden="true"><g fill="none" stroke="var(--orange)" stroke-width="1.4"><circle cx="8" cy="8" r="6.5"/><ellipse cx="8" cy="8" rx="3" ry="6.5"/><path d="M1.5 8h13M3 4.5h10M3 11.5h10"/></g></svg>
        www.yourwebsite.com
      </li>
    </ul>
  </div>
</section>

</body>
</html>
```